Web Design for an Online Dating Web Site

We need an uncoded web design for a new online dating web site called zMatchy.net. Simplicity and boldness are the key factors in the successful design.
Please look at the requirements document attached for details.
Updates
Dear all,
Please AVOID USING A PICTURE OF A HAPPY COUPLE ON THE HOME PAGE of the site. We highly want to move away from this space as it makes our web site just like another dating web site.
We like something simple with web 2.0 look and feel. The examples in the Requirements Document are exactly the design we are after.
Regards
Tarn
Industry/Entity Type
Dating
Look and feel
Each slider illustrates characteristics of the customer's brand and the style your logo design should communicate.

```html
<!DOCTYPE html>
<html lang="en">
<head>
<meta charset="utf-8">
<title>zMatchy.net – Home</title>
<link href="https://fonts.googleapis.com/css2?family=Open+Sans:wght@400;600;700&family=Kristi&display=swap" rel="stylesheet">
<style>
:root{
  --page:#ffffff;
  --panel:#2b2c33;
  --deep:#1c1c20;
  --box:#363740;
  --field:#25262c;
  --rule:#55565e;
  --pink:#ec2a8a;
  --pink-light:#f65aa6;
  --pink-dark:#c90f6d;
  --text:#b9bac0;
  --muted:#8c8d94;
  --script:"Kristi", cursive;
  --sans:"Open Sans", Arial, sans-serif;
}
*{box-sizing:border-box;margin:0;padding:0}
html,body{width:1200px;height:901px;overflow:hidden;background:var(--page);font-family:var(--sans)}
.site{position:absolute;left:251px;top:0;width:698px;height:901px;background:var(--panel)}
.abs{position:absolute}
.header{left:0;top:0;width:698px;height:102px;border-bottom:1px solid var(--rule)}
.brand{left:69px;top:24px;display:flex;align-items:center;gap:8px;color:var(--pink);font-weight:700;font-size:40px;letter-spacing:-1px}
.brand-dot{width:14px;height:14px;border-radius:50%;background:var(--pink)}
.nav{right:69px;top:86px;display:flex;gap:28px;font-size:8px;color:var(--text)}
.nav .active{color:var(--pink)}
.loginbar{left:0;top:103px;width:698px;height:48px;border-bottom:1px solid #111}
.field{height:21px;background:var(--field);border-radius:2px;box-shadow:0 1px 2px #000;color:var(--text);font-size:10px;font-weight:600;padding:5px 6px}
.btn{background:linear-gradient(var(--pink-light),var(--pink-dark));color:#fff;border-radius:3px;font-weight:700;text-align:center;box-shadow:0 1px 2px #000}
.or{left:342px;top:116px;font-family:var(--script);font-size:20px;color:var(--text)}
.social{top:118px;width:26px;height:26px;border-radius:50%;background:linear-gradient(var(--pink-light),var(--pink-dark));color:#fff;font-size:7px;font-weight:700;text-align:center;line-height:26px}
.hero{left:0;top:151px;width:698px;height:211px;background:var(--deep);border-bottom:1px solid var(--rule)}
.slide{left:124px;top:25px;width:449px;height:164px;background:var(--box);border-radius:10px;box-shadow:0 2px 4px #000;display:flex;align-items:center;justify-content:center;font-family:var(--script);color:var(--pink);font-size:34px}
.arrow{top:93px;width:28px;height:28px}
.video{left:124px;top:388px;width:218px;height:164px;background:var(--box);border-radius:8px;box-shadow:0 2px 4px #000}
.video-art{position:absolute;left:38px;top:30px;width:142px;height:128px;background:radial-gradient(#6e3a57,#4a3040);border-radius:50% 50% 45% 45%}
.play{left:95px;top:68px}
.signup{left:178px;top:568px;width:110px;height:42px;border-radius:4px;font-family:var(--script);font-size:28px;line-height:42px;font-weight:400}
.divider{left:438px;top:363px;width:1px;height:258px;background:#777}
.blog-title{left:462px;top:382px;font-family:var(--script);color:var(--pink);font-size:27px}
.post{left:462px;display:flex;gap:14px}
.thumb{width:28px;height:28px;background:var(--box);box-shadow:0 1px 3px #000;border-radius:2px}
.post h3{font-size:8px;font-weight:600;color:var(--pink);width:112px;line-height:10px}
.post p{font-size:5px;color:var(--text);margin-top:2px}
.footer{left:0;top:632px;width:698px;height:239px;background:var(--deep)}
.foot-brand{left:293px;top:19px;color:var(--pink);font-weight:700;font-size:22px;display:flex;gap:5px;align-items:center}
.foot-brand .brand-dot{width:8px;height:8px}
.foot-head{font-family:var(--script);color:var(--pink);font-size:17px}
.links{left:124px;top:87px;list-style:none;font-size:10px;font-weight:600;color:var(--text)}
.links li{height:24.5px}
.sq{top:86px;width:18px;height:18px;border-radius:3px;background:#6c7fb0}
.fbox{background:var(--field);border:1px solid #000;border-radius:3px;color:var(--text);font-size:8px;padding:3px 5px}
.send{left:579px;top:198px;width:49px;height:22px;font-family:var(--script);font-size:20px;line-height:22px;font-weight:400;border-radius:2px}
.bottombar{left:0;top:871px;width:698px;height:30px;font-size:8px;color:var(--text)}
</style>
</head>
<body>
<div class="site">
  <header class="abs header">
    <div class="abs brand"><span>zMatchy</span><span class="brand-dot"></span></div>
    <nav class="abs nav"><span class="active">Home</span><span>Why</span><span>How it Works</span><span>Our Blog</span><span>Sign Up</span></nav>
  </header>

  <section class="abs loginbar"></section>
  <div class="abs field" style="left:69px;top:120px;width:98px">Email:</div>
  <div class="abs field" style="left:172px;top:120px;width:98px">Password:</div>
  <div class="abs btn" style="left:275px;top:120px;width:55px;height:22px;font-size:10px;line-height:22px">Log In</div>
  <span class="abs or">or</span>
  <span class="abs social" style="left:370px"></span>
  <span class="abs social" style="left:417px"></span>
  <span class="abs social" style="left:463px"></span>
  <span class="abs social" style="left:509px"></span>
  <span class="abs social" style="left:556px"></span>
  <span class="abs social" style="left:601px">More...</span>

  <section class="abs hero">
    <svg class="abs arrow" style="left:70px" viewBox="0 0 28 28"><circle cx="14" cy="14" r="13" fill="#ec2a8a" stroke="#a80d5b"/><path d="M17 8 L9 14 L17 20Z" fill="#333"/></svg>
    <div class="abs slide">Why we are different</div>
    <svg class="abs arrow" style="left:601px" viewBox="0 0 28 28"><circle cx="14" cy="14" r="13" fill="#ec2a8a" stroke="#a80d5b"/><path d="M11 8 L19 14 L11 20Z" fill="#333"/></svg>
  </section>

  <div class="abs video">
    <div class="video-art" role="img" aria-label="Large faded heart illustration behind the video"></div>
    <svg class="abs play" width="28" height="28" viewBox="0 0 28 28"><circle cx="14" cy="14" r="13" fill="#ec2a8a" stroke="#a80d5b"/><path d="M11 8 L19 14 L11 20Z" fill="#333"/></svg>
  </div>
  <div class="abs btn signup">Sign Up</div>

  <div class="abs divider"></div>
  <h2 class="abs blog-title" style="font-weight:400">Latest Blog Posts</h2>
  <article class="abs post" style="top:425px"><span class="thumb"></span><div><h3>Owen &amp; Lila get hitched</h3><p>October 3rd 2011 | 3 comments | Read</p></div></article>
  <article class="abs post" style="top:466px"><span class="thumb"></span><div><h3>Romance in the 21st centuary</h3><p>October 2nd 2011 | 7 comments | Read</p></div></article>
  <article class="abs post" style="top:508px"><span class="thumb"></span><div><h3>Another Blog Heading</h3><p>September 29th | 2011 | 3 comments | Read</p></div></article>
  <article class="abs post" style="top:552px"><span class="thumb"></span><div><h3>And another</h3><p>September 9th | 2011 | 12 comments | Read</p></div></article>

  <footer class="abs footer">
    <div class="abs foot-brand"><span>zMatchy</span><span class="brand-dot"></span></div>
    <h4 class="abs foot-head" style="left:124px;top:60px;font-weight:400">Read more...</h4>
    <ul class="abs links"><li>Why zMatchy</li><li>How it Works</li><li>Sign Up</li><li>Login</li><li>About Us</li></ul>
    <h4 class="abs foot-head" style="left:324px;top:60px;font-weight:400">Follow us...</h4>
    <span class="abs sq" style="left:306px"></span>
    <span class="abs sq" style="left:340px;background:#555"></span>
    <span class="abs sq" style="left:374px;background:#3aa6dc"></span>
    <h4 class="abs foot-head" style="left:478px;top:60px;font-weight:400">Let's Talk...</h4>
    <div class="abs fbox" style="left:478px;top:88px;width:150px;height:17px">Name</div>
    <div class="abs fbox" style="left:478px;top:107px;width:150px;height:17px">Email</div>
    <div class="abs fbox" style="left:478px;top:126px;width:150px;height:69px">Comments</div>
    <div class="abs btn send">Send</div>
  </footer>

  <div class="abs bottombar">
    <span class="abs" style="left:69px;top:9px">Privacy | Terms &amp; Conditions</span>
    <span class="abs" style="right:69px;top:10px">©2011 zMatchy</span>
  </div>
</div>
</body>
</html>
```